QAMARIN AL-RIYAH MEDICAL CO
QAMARIN AL-RIYAH
Project: QAMARIN AL-RIYAH MEDICAL CO
QAMARIN AL-RIYAH MEDICAL CO - Pharmacy/Pharmaceuticals
Creative Brief
Use same font as used in my logo
HUDA KERMANI
Sales & Marketing Director
P.O Box 4137 Dammam 31276 Saudi Arabia
huda@qrm.med.example
www.qrm.med.example

```html
<!DOCTYPE html>
<html lang="en">
<head>
<meta charset="utf-8">
<title>Qamarin Al-Riyah Medical Co – Business Card</title>
<link href="https://fonts.googleapis.com/css2?family=Didact+Gothic&display=swap" rel="stylesheet">
<style>
  :root {
    --bg: #e6e4e0;
    --card: #ffffff;
    --green: #6a9a1f;
    --green-faint: #dfe9cc;
    --grey: #8a8a8a;
    --grey-dark: #4a4a4a;
    --grey-faint: #e9e9e9;
  }
  * { box-sizing: border-box; margin: 0; padding: 0; }
  html, body { width: 1200px; height: 904px; overflow: hidden; }
  body {
    background: var(--bg);
    font-family: "Didact Gothic", "Century Gothic", sans-serif;
    position: relative;
  }
  .card {
    position: absolute;
    width: 600px;
    height: 343px;
    background: var(--card);
    border-radius: 14px;
    overflow: hidden;
    box-shadow: 0 6px 18px rgba(0,0,0,.18);
  }
  .card--back { left: 60px; top: 80px; }
  .card--front { left: 540px; top: 480px; }

  /* back side */
  .back-mark {
    position: absolute; left: -30px; top: 40px;
    width: 250px; height: 250px; border-radius: 50%;
    background: var(--green-faint); opacity: .7;
  }
  .back-name {
    position: absolute; left: 30px; top: 150px;
    font-size: 30px; letter-spacing: 1px; color: var(--grey-faint);
  }
  .back-web {
    position: absolute; right: 34px; top: 168px;
    font-size: 12px; letter-spacing: 4px; color: var(--grey-dark);
  }

  /* front side */
  .swoosh { position: absolute; inset: 0; width: 600px; height: 343px; }
  .brand {
    position: absolute; left: 42px; top: 44px;
    display: flex; align-items: center; gap: 12px;
    color: var(--green);
  }
  .brand__dot { width: 30px; height: 30px; border-radius: 50%; background: var(--green); }
  .brand__name { font-size: 24px; letter-spacing: .5px; line-height: 1; }
  .brand__sub { font-size: 10px; letter-spacing: 3px; margin-top: 4px; }

  .person { position: absolute; left: 340px; top: 96px; text-align: left; }
  .person__name { font-size: 17px; color: var(--green); letter-spacing: .5px; }
  .person__title { font-size: 12px; color: var(--grey-dark); margin-top: 3px; }

  .address {
    position: absolute; left: 44px; top: 170px;
    font-size: 12px; line-height: 16px; color: var(--grey-dark);
  }
  .contacts {
    position: absolute; left: 44px; top: 232px;
    list-style: none; font-size: 12px; line-height: 16px; color: var(--grey-dark);
  }
  .contacts li { display: flex; align-items: center; gap: 8px; }
  .contacts svg { width: 11px; height: 11px; fill: var(--green); flex: none; }
</style>
</head>
<body>

  <section class="card card--back" aria-label="Card back">
    <div class="back-mark"></div>
    <div class="back-name">QAMARIN AL-RIYAH</div>
    <div class="back-web">www.qrm.med.example</div>
  </section>

  <section class="card card--front" aria-label="Card front">
    <svg class="swoosh" viewBox="0 0 600 343" aria-hidden="true">
      <path d="M400,0 C520,60 560,200 470,343 L520,343 C600,220 570,80 450,0 Z" fill="var(--grey)"/>
      <path d="M470,0 L600,0 L600,240 C600,140 560,50 470,0 Z" fill="var(--green)"/>
    </svg>

    <div class="brand">
      <span class="brand__dot"></span>
      <div>
        <div class="brand__name">QAMARIN AL-RIYAH</div>
        <div class="brand__sub">MEDICAL CO</div>
      </div>
    </div>

    <div class="person">
      <div class="person__name">HUDA KERMANI</div>
      <div class="person__title">Sales &amp; Marketing Director</div>
    </div>

    <address class="address" style="font-style:normal">
      P.O Box 4137<br>Dammam 31276<br>Saudi Arabia
    </address>

    <ul class="contacts">
      <li><svg viewBox="0 0 10 10"><rect x="1" y="3" width="8" height="6" rx="1"/><rect x="2" y="1" width="6" height="2"/></svg>+966130000412</li>
      <li><svg viewBox="0 0 10 10"><rect x="2.5" y="0" width="5" height="10" rx="1"/></svg>+966550000367</li>
      <li><svg viewBox="0 0 10 10"><rect x="1" y="2" width="8" height="7"/><rect x="3" y="0" width="4" height="2"/></svg>+966130000413</li>
      <li><svg viewBox="0 0 10 10"><rect x="0" y="2" width="10" height="6"/></svg>huda@qrm.med.example</li>
      <li><svg viewBox="0 0 10 10"><circle cx="5" cy="5" r="4.5"/></svg>www.qrm.med.example</li>
    </ul>
  </section>

</body>
</html>
```